Buch-/E-Book-Cover für eine Kriminalgeschichte Mittelfrankens
Der Designer überzeugte schon mit dem ersten Entwurf des Covers. Es gab danach nur noch marginale Änderungswünsche meinerseits, die stets schnell und komplikationslos durchgeführt wurden. Dieses Cover entspricht genau meinen Vorstellungen und ist auch in meinem Bekanntenkreis der Favorit gewesen. Ich würde jederzeit wieder von diesem Designer grafische Arbeiten durchführen lassen.
Zielgruppe
Eigentlich bin ich Polizist, habe aber nun ein Buch über die Kriminalgeschichte Mittelfrankens geschrieben. In 80 echten Fällen beschreibe ich darin die Entwicklung der polizeilichen Ermittlungsarbeit zwischen 1917 und 2011. Mein Dienstort ist Nürnberg, ich bin auch ein geborener Nürnberger. Meine Zielgruppe werden wohl die Einwohner Mittelfrankens sein, vor allem aber viele Kollegen und Polizeipensionisten
Aufgabenstellung
Das Buch hat lokalen Bezug zu Mittelfranken, beinhaltet aber auch Kriminalfälle, die bundesweit Schlagzeilen machten. 'Der Glockenmann', Festnahme und Tod einer GLK-Terroristin in Nürnberg, Dammbruchkatastrophe von Nürnberg-Katzwang, die ZELT-Massenverhaftungen, Amoklauf eines Neonazi, Kampfbund Leitner: das sind einige Beispiele, die in den nationalen und teilweise auch in den internationalen Zeitungen erschienen sind.

```html
<!DOCTYPE html>
<html lang="de">
<head>
<meta charset="utf-8">
<title>Akte Franken – Buchcover</title>
<link rel="stylesheet" href="https://fonts.googleapis.com/css2?family=Roboto+Slab:wght@300;400;700&display=swap">
<style>
  :root {
    --page-bg: #ffffff;
    --cover-black: #000000;
    --signal-yellow: #ffe600;
    --title-red: #c8102e;
    --text-white: #ffffff;
    --photo-light: #f4f4f4;
    --photo-mid: #d9d9d9;
  }
  * { margin: 0; padding: 0; box-sizing: border-box; }
  html, body {
    width: 1200px; height: 1058px; overflow: hidden;
    background: var(--page-bg);
  }
  .canvas { position: relative; width: 1200px; height: 1058px; }
  .book-cover {
    position: absolute; left: 347px; top: 65px;
    width: 559px; height: 869px;
    background: var(--cover-black);
    font-family: "Roboto Slab", Rockwell, Georgia, serif;
    font-variant-numeric: lining-nums;
    color: var(--text-white);
    text-align: center;
  }
  .author-name {
    position: absolute; left: 0; right: 0; top: 45px;
    font-weight: 700; font-size: 31px; letter-spacing: 0.2em;
    line-height: 1; padding-left: 0.2em;
  }
  .rule {
    position: absolute; left: 0; right: 0; height: 4px;
    background: var(--signal-yellow);
  }
  .rule--top { top: 92px; }
  .rule--middle { top: 404px; }
  .rule--bottom { top: 790px; }
  .title-block { position: absolute; left: 0; right: 0; top: 128px; font-size: inherit; }
  .title-accent {
    display: block; color: var(--title-red);
    font-weight: 700; font-size: 52px; line-height: 56px;
  }
  .title-line {
    display: block; font-weight: 300;
    font-size: 39px; line-height: 47px;
  }
  .subtitle-line {
    display: block; font-weight: 300;
    font-size: 34px; line-height: 46px; margin-top: 4px;
  }
  .case-count {
    display: block; color: var(--title-red);
    font-weight: 700; font-size: 58px; line-height: 62px;
  }
  .cover-photo {
    position: absolute; left: 0; right: 0; top: 424px; height: 354px;
    background: radial-gradient(ellipse at 45% 60%, var(--photo-light) 0%, #ebebeb 55%, var(--photo-mid) 100%);
  }
  .publisher {
    position: absolute; left: 0; right: 0; top: 806px;
    font-weight: 400; font-size: 27px; line-height: 36px;
  }
</style>
</head>
<body>
<main class="canvas">
  <section class="book-cover">
    <h2 class="author-name">KURT WOLKENHAINER</h2>
    <div class="rule rule--top"></div>
    <h1 class="title-block">
      <span class="title-accent">»Akte Franken</span>
      <span class="title-line">Polizeigeschichte</span>
      <span class="title-line">rund um Nürnberg«</span>
      <span class="subtitle-line">Erzählt in</span>
      <span class="case-count">80 Akten</span>
    </h1>
    <div class="rule rule--middle"></div>
    <div class="cover-photo" role="img" aria-label="Schwarzweißfoto eines Tatorts: Fingerabdrücke auf weißer Fläche, eine Spurennummer 1 und ein Maßstablineal der Spurensicherung"></div>
    <div class="rule rule--bottom"></div>
    <p class="publisher">lindhof-verlag</p>
  </section>
</main>
</body>
</html>
```